Small business services company needs a flyer designed

We need a flyer designed for a small building services company who has multiple roles ie- Roof, gutter and pressure cleaning, small building maintenance and garden cleanups. The company is based in Far North Queensland (Australia) where it is a tropical climate with lots of trees and green areas.

I want the colours to be based on the Logo and business card colours which will be added.

The flyer will need to be changeable so I can create monthly specials ie- Roof Cleaning Special, Gutter Cleaning Special or Pressure Cleaning special.

The roles of the business will be as stated on the attached business card.
Updates

Good evening all designers, please find below an update for you all, I hope it may answer some questions you have.

'd like the flyer to be DL size and at present I don't have any photo's. But i'd be happy for you to source some from google. The pictures I'd like would be of gutter cleaning from a ladder, pressure washing roofs & driveways with the large round "flat surface cleaners". Possibly have split pictures of the pressure cleaning to show before and after. 
Far North Queensland is a very tropical environment that has lots of palm trees and rain forest. The climate is usually 30+ degrees C. Incorporating those colours with the logo colours I'd like. 

Hello all designers.

I have just uploaded some of my own job pictures. There is a before and an after picture. If you source any other pictures, I'd like to see a flat surface/ spindeck cleaner in operation, either on a roof or a driveway.

My goal is for a single sided flyer with all the details from my business card to be on the flyer. 

Please remember the climate in my area is very tropical and usually 30+ degrees C. Never cold or snowing. So please have pictures to reflect.

Thanks for the designs.
Regards,Glenn

Reason: hi all designers. I have extended the deadline by 3 days to accommodate all the designers who have only recently accepted the craft hive invites. I have had a lot of declines and want the best designs I can choice from. This is no reflection of the calibre of the designs I have already received. I look forward to seeing all the updates and new designs. Regards, Glenn

Target Market(s)

Home owners who take pride in the street appeal of their homes, or to add value to their selling price when a house goes on the sales market.

Industry/Entity Type

Building

```html
<!DOCTYPE html>
<html lang="en">
<head>
<meta charset="utf-8">
<title>Upreach – Roof, Gutter &amp; Pressure Cleaning Flyer</title>
<link href="https://fonts.googleapis.com/css2?family=Comfortaa:wght@500;700&family=Didact+Gothic&family=Delius&display=swap" rel="stylesheet">
<style>
  :root{
    --green:#3fdc8c;
    --green-dark:#2fc47a;
    --palm:#5fe3a0;
    --cream:#f6f1cf;
    --ring:#f3f0dc;
    --navy:#1a2a8c;
    --ink:#3a3a3a;
    --white:#ffffff;
  }
  *{margin:0;padding:0;box-sizing:border-box}
  html,body{width:1200px;height:600px;overflow:hidden;background:var(--white)}
  .flyer{position:relative;width:1200px;height:600px;overflow:hidden;background:var(--white);font-family:'Comfortaa',sans-serif}
  .backdrop{position:absolute;inset:0}
  .txt{position:absolute;white-space:nowrap}
  .brand-name{left:28px;top:52px;font-family:'Didact Gothic',sans-serif;font-size:72px;letter-spacing:2px;color:var(--green-dark);line-height:1}
  .brand-dot{position:absolute;left:345px;top:40px;width:70px;height:70px;border-radius:50%;background:var(--navy)}
  .brand-tagline{left:28px;top:128px;font-family:'Didact Gothic',sans-serif;font-size:12.5px;color:var(--navy);font-weight:700;letter-spacing:.2px}
  .brand-phone{left:90px;top:143px;font-family:'Didact Gothic',sans-serif;font-size:15px;color:var(--green-dark);font-weight:700}
  .owner-name{left:27px;top:180px;font-family:'Didact Gothic',sans-serif;font-size:19px;color:var(--navy)}
  .owner-role{left:27px;top:205px;font-family:'Didact Gothic',sans-serif;font-size:14px;color:var(--navy)}
  .job-types{left:27px;top:232px;font-family:'Didact Gothic',sans-serif;font-size:17px;color:var(--ink);line-height:1.35}
  .service{color:var(--white);font-size:17px;text-align:center;line-height:1.2}
  .bubble{position:absolute;border-radius:50%;background:var(--white);display:flex;align-items:center;justify-content:center;text-align:center;font-family:'Delius',sans-serif;color:var(--green-dark);font-size:16px;line-height:1.15}
  .bubble--waste{left:60px;top:366px;width:104px;height:104px;font-size:14px}
  .bubble--complex{left:234px;top:415px;width:122px;height:122px;font-size:18px}
  .bubble--gutter{left:410px;top:365px;width:96px;height:96px}
  .offer{position:absolute;color:var(--white);font-family:'Delius',sans-serif;text-align:center;transform:rotate(12deg)}
  .offer-big{left:728px;top:118px;font-size:21px}
  .offer-small{left:708px;top:160px;font-size:15px;line-height:1.35}
  .cert{position:absolute;left:962px;top:384px;width:190px;text-align:center;color:var(--white);font-family:'Delius',sans-serif;font-size:17px;line-height:1.3;transform:rotate(-17deg)}
  .photo-label{position:absolute;color:var(--white);font-family:'Comfortaa',sans-serif;font-size:13px}
  .footer{position:absolute;left:0;top:562px;width:640px;height:38px;background:var(--cream)}
  .footer-text{position:absolute;top:572px;font-family:'Comfortaa',sans-serif;font-size:15px;color:var(--green-dark)}
</style>
</head>
<body>
<main class="flyer">
  <svg class="backdrop" width="1200" height="600" viewBox="0 0 1200 600">
    <defs>
      <radialGradient id="palm-tone" cx="0.5" cy="0.55" r="0.5">
        <stop offset="0" stop-color="var(--palm)" stop-opacity=".85"/>
        <stop offset=".65" stop-color="var(--palm)" stop-opacity=".45"/>
        <stop offset="1" stop-color="var(--palm)" stop-opacity="0"/>
      </radialGradient>
      <linearGradient id="after-tone" x1="0" y1="0" x2="0" y2="1">
        <stop offset="0" stop-color="#9a9a8a"/><stop offset="1" stop-color="#cfcab0"/>
      </linearGradient>
      <linearGradient id="before-tone" x1="0" y1="0" x2="0" y2="1">
        <stop offset="0" stop-color="#4a6a3a"/><stop offset="1" stop-color="#2a2a2a"/>
      </linearGradient>
    </defs>
    <rect class="top-band" x="0" y="0" width="1200" height="15" fill="var(--green)"/>
    <circle cx="880" cy="300" r="340" fill="var(--ring)"/>
    <circle cx="880" cy="300" r="290" fill="var(--white)"/>
    <circle cx="880" cy="300" r="265" fill="var(--ring)"/>
    <ellipse cx="540" cy="250" rx="200" ry="130" fill="url(#palm-tone)" role="img" aria-label="Palm tree silhouettes"/>
    <circle cx="300" cy="690" r="430" fill="var(--green)"/>
    <circle cx="770" cy="160" r="100" fill="var(--green)"/>
    <circle cx="1060" cy="420" r="108" fill="var(--green)"/>
    <circle cx="1010" cy="215" r="134" fill="var(--green)"/>
    <circle cx="1010" cy="215" r="124" fill="url(#after-tone)" role="img" aria-label="Photo: concrete stairs after pressure cleaning"/>
    <circle cx="790" cy="420" r="122" fill="var(--green)"/>
    <circle cx="790" cy="420" r="112" fill="url(#before-tone)" role="img" aria-label="Photo: dark stained stairs before pressure cleaning"/>
  </svg>

  <span class="brand-dot" aria-hidden="true"></span>
  <h1 class="txt brand-name">UPREACH</h1>
  <p class="txt brand-tagline">ROOF, GUTTER &amp; PRESSURE CLEANING SERVICES</p>
  <p class="txt brand-phone">CALL 0400 123 456</p>

  <p class="txt owner-name">Glenn Harwood</p>
  <p class="txt owner-role">Owner operator</p>
  <p class="txt job-types">Residential, Commercial &amp;<br>Body Corporate Jobs</p>

  <p class="txt service" style="left:195px;top:330px">Minor Roof, Gutter &amp;<br>Building Maintenance</p>
  <p class="txt service" style="left:62px;top:505px;transform:rotate(-4deg)">Driveways</p>
  <p class="txt service" style="left:392px;top:488px;transform:rotate(4deg)">Pressure Cleaning<br>-Roof's</p>

  <div class="bubble bubble--waste">Garden Waste<br>Removal</div>
  <div class="bubble bubble--complex">Complex<br>Cleanups</div>
  <div class="bubble bubble--gutter">Gutter<br>Cleaning</div>

  <p class="offer offer-big">10% Discount</p>
  <p class="offer offer-small">for Emergency<br>Services,<br>Defence &amp; Seniors</p>

  <p class="photo-label" style="left:985px;top:346px">After</p>
  <p class="photo-label" style="left:780px;top:512px">Before</p>

  <p class="cert">National Working at Heights Certification</p>

  <div class="footer"></div>
  <p class="footer-text" style="left:45px">ABN - 12 345 678 901</p>
  <p class="footer-text" style="left:244px">|</p>
  <p class="footer-text" style="left:305px">jobs@upreachclean.com.au</p>
</main>
</body>
</html>
```